Heron Trade finance web design

We are a newly established business which provides invoice finance to Small Businesses in England and Wales.
Our approach is very much a funder where the small business owner can talk to the decision maker. We will guarantee on receipt of information, a decision within 24 hours.
We are not a bank so the look of the website need to be friendly but professional.
Have two types of people we are trying to attract to the website: 1) partners who are small business owners and 2) introducers who is accountants and commercial brokers who introduce us to the small businesses.
Currently no website, although domain has been reserved.
The design should be:
Professional
“Clean” Look
Designed to convey Trust and Authority.
Appeal to the small business owner.
Must incorporate:
Logo (attached)
Front page:Top tabs to other pages 1) About us 2) Services 3) Introducers 4) Contact us
Need picture and logo on page.
1) About us page- Room for talk about the company, the people and our critera.
2) Services page- We need for what invoice finance is, and 5 boxes for different services we will provide. (link on page to contact us)
3) Introducers page- We need a part for why become an introducer? Who we can help? Why we are different? (link on page to contact us)
4) Contact us page- Office address, email, tel and if possible a map and a contact me part which will email direct to us.
Text will be provided for the design, if we can see the setup of the website we will provide a part for each of the pages to support.
Styles we think convey the correct image:
www.brindlecapital.example
www.tollmarkfs.example
www.qelfunding.example
Small business owners
Finance
5+ page

```html
<!DOCTYPE html>
<html lang="en">
<head>
<meta charset="utf-8">
<title>Heron Trade Finance</title>
<link href="https://fonts.googleapis.com/css2?family=Roboto:wght@400;500;700&family=Arimo:wght@400;700&family=Lato:wght@300;400&display=swap" rel="stylesheet">
<style>
:root{
  --red:#e4353b;
  --red-dark:#c9252b;
  --ink:#2a2a2a;
  --grey-text:#8e8e8e;
  --panel:#efefef;
  --field:#ececec;
  --field-line:#cfcfcf;
  --footer:#262626;
  --white:#ffffff;
}
*{margin:0;padding:0;box-sizing:border-box}
html,body{width:1200px;height:2740px;overflow:hidden}
body{position:relative;background:var(--white);font-family:"Arimo",Arial,sans-serif;color:var(--ink)}
.abs{position:absolute}
.pill{position:absolute;display:flex;align-items:center;justify-content:center;border-radius:999px;font-family:"Roboto",sans-serif;text-transform:uppercase;color:var(--white)}
.pill.solid{background:var(--red)}
.pill.ghost{border:2px solid var(--white)}

/* header */
.topline{position:absolute;left:0;top:0;width:1200px;height:5px;background:var(--ink)}
.brand{position:absolute;left:78px;top:36px;font-family:"Roboto",sans-serif;font-weight:700;font-size:34px;color:var(--red);line-height:48px}
.nav a{position:absolute;top:40px;height:46px;line-height:46px;font-family:"Roboto",sans-serif;font-size:16px;color:var(--ink);text-decoration:none}
.nav .current{left:475px;width:98px;text-align:center;background:var(--red);color:var(--white);border-radius:23px}

/* hero */
.hero{position:absolute;left:0;top:119px;width:1200px;height:562px;
  background:linear-gradient(90deg,#8aa2b8 0%,#b9c7d4 28%,#dfe6ec 55%,#eef1f4 100%)}
.hero-title{position:absolute;right:75px;top:174px;font-family:"Lato",sans-serif;font-weight:300;font-size:55px;color:var(--white);text-align:right}
.hero-text{position:absolute;right:75px;top:246px;width:640px;font-size:14.5px;line-height:28px;color:#2e2e2e;text-align:right}
.hero-arrow{position:absolute;top:244px;width:52px;height:52px;border:2px solid #333;border-radius:50%;display:flex;align-items:center;justify-content:center}

/* section titles */
.section-title{position:absolute;left:0;width:1200px;text-align:center;font-family:"Roboto",sans-serif;font-size:40px;text-transform:uppercase;color:var(--ink)}
.section-title span{color:var(--red)}
.lede{position:absolute;left:150px;width:900px;text-align:center;font-size:13.5px;line-height:27px;color:var(--grey-text)}

/* services */
.services{position:absolute;left:0;top:1055px;width:1200px;height:450px;background:var(--panel)}
.service{position:absolute;top:133px;width:210px;text-align:center}
.service .icon{width:114px;height:114px;margin:0 auto;border-radius:50%;background:var(--white);border:1px solid #d4d4d4;display:flex;align-items:center;justify-content:center}
.service.active .icon{background:var(--red);border-color:var(--red)}
.service h3{margin-top:18px;font-family:"Roboto",sans-serif;font-weight:400;font-size:18px;color:var(--ink)}
.service.active h3{color:var(--red)}
.service p{margin-top:10px;font-size:13.5px;line-height:25px;color:var(--grey-text)}
.service .more{margin-top:10px}

/* introducers */
.introducers{position:absolute;left:0;top:1505px;width:1200px;height:436px;background:var(--red)}
.introducers .section-title{color:var(--ink)}
.introducers .section-title span{color:var(--white)}
.intro-col{position:absolute;top:140px;width:340px;color:var(--white)}
.intro-col h4{font-family:"Roboto",sans-serif;font-weight:400;font-size:16.5px;text-transform:uppercase;display:flex;align-items:center;gap:10px}
.intro-col h4 b{font-size:22px;color:var(--ink)}
.intro-col p{margin-top:14px;font-size:13.5px;line-height:27px}
.intro-col .pill{position:relative;width:177px;height:55px;margin-top:18px;font-size:19px}
.intro-divider{position:absolute;top:140px;width:18px;height:260px;background:linear-gradient(90deg,rgba(0,0,0,.07),rgba(0,0,0,0))}

/* contact */
.field{position:absolute;background:var(--field);border:1px solid var(--field-line);font-size:15px;color:#777;padding:14px 12px}
.field.focus{border:2px solid var(--red);color:var(--red)}

/* footer */
.footer{position:absolute;left:0;top:2414px;width:1200px;height:268px;background:var(--footer);color:var(--white)}
.footer h5{position:absolute;top:30px;font-family:"Roboto",sans-serif;font-weight:400;font-size:18px;color:var(--red);text-transform:uppercase}
.links{position:absolute;left:78px;top:80px;list-style:none;font-size:14px;line-height:27px}
.links li::before{content:"» ";margin-right:6px}
.touch{position:absolute;left:343px;top:76px;width:240px;font-size:14px;line-height:21px}
.touch .row{display:flex;gap:16px;margin-bottom:14px}
.map{position:absolute;left:608px;top:69px;width:247px;height:165px;background:linear-gradient(135deg,#e8e4d8,#d9dcc9 60%,#cfd8d9)}
.newsletter-text{position:absolute;left:873px;top:72px;width:260px;font-size:14px;line-height:21px}
.email-input{position:absolute;left:873px;top:141px;width:248px;height:40px;background:var(--white);color:#444;font-size:14px;padding:11px 14px}
.copyright{position:absolute;left:0;top:2682px;width:1200px;height:58px;background:var(--red);color:var(--white);font-size:13.5px;text-align:center;line-height:58px}
.copyright b{color:var(--ink)}
</style>
</head>
<body>

<div class="topline"></div>
<div class="brand">Heron Trade Finance</div>
<nav class="nav">
  <a class="current" href="#">HOME</a>
  <a href="#" style="left:614px">ABOUT US</a>
  <a href="#" style="left:738px">SERVICES</a>
  <a href="#" style="left:860px">INTRODUCERS</a>
  <a href="#" style="left:1017px">CONTACT US</a>
</nav>

<section class="hero" role="img" aria-label="Photo of a smiling businessman in a striped shirt working on a laptop in a bright office">
  <div class="hero-arrow" style="left:12px"><svg width="16" height="22" viewBox="0 0 16 22"><path d="M12 2 3 11l9 9" fill="none" stroke="#333" stroke-width="2.5"/></svg></div>
  <div class="hero-arrow" style="right:12px"><svg width="16" height="22" viewBox="0 0 16 22"><path d="M4 2l9 9-9 9" fill="none" stroke="#333" stroke-width="2.5"/></svg></div>
  <h1 class="hero-title">Trade Finance Limited</h1>
  <p class="hero-text">Lorem Ipsum is simply dummy text of the printing and typesetting industry. Lorem Ipsum has been the industry's standard dummy text ever since the&nbsp; when an unknown printer took a galley of type and scrambled it to make a specimen book.</p>
  <div class="pill solid" style="left:860px;top:337px;width:261px;height:61px;font-family:'Lato',sans-serif;font-size:21px">Contact us know</div>
</section>

<h2 class="section-title" style="top:730px">Welcome to <span>Heron</span></h2>
<p class="lede" style="top:792px">Lorem Ipsum is simply dummy text of the printing and typesetting industry. Lorem Ipsum has been the industry's standard dummy text ever since the 1500s, when an unknown printer took a galley of type and scrambled it to make a type specimen book.<br>It has survived not only five centuries. Lorem Ipsum is simply dummy text of the printing and typesetting industry. Lorem Ipsum has been the industry's standard dummy text ever since the 1500s, when an unknown printer took a galley of type and scrambled it to make a type specimen book. It has survived not only five centuries.</p>
<div class="pill solid" style="left:511px;top:939px;width:176px;height:54px;font-size:20px">Know more</div>

<section class="services">
  <h2 class="section-title" style="top:55px">Our <span>Services</span></h2>

  <div class="service" style="left:78px">
    <div class="icon"><svg width="64" height="54" viewBox="0 0 64 54"><rect x="4" y="36" width="8" height="16" fill="#333"/><rect x="16" y="28" width="8" height="24" fill="#333"/><rect x="28" y="32" width="8" height="20" fill="#333"/><rect x="40" y="20" width="8" height="32" fill="#333"/><rect x="52" y="12" width="8" height="40" fill="#333"/><path d="M4 30 20 16l10 8L54 4" fill="none" stroke="#333" stroke-width="4"/><path d="M46 2h12v12" fill="none" stroke="#333" stroke-width="4"/></svg></div>
    <h3>SERVICES ONE</h3>
    <p>Lorem Ipsum is simply text of dummy text of the printing and type setting..</p>
    <svg class="more" width="18" height="18" viewBox="0 0 18 18"><path d="M3 3l6 5 6-5M3 10l6 5 6-5" fill="none" stroke="#333" stroke-width="2"/></svg>
  </div>

  <div class="service" style="left:288px">
    <div class="icon"><svg width="54" height="60" viewBox="0 0 54 60"><rect x="8" y="3" width="38" height="50" rx="3" fill="none" stroke="#333" stroke-width="3"/><path d="M16 14h22M16 22h22M28 30h10M28 38h10" stroke="#333" stroke-width="3"/><circle cx="16" cy="44" r="9" fill="#333"/><path d="M12 44l3 3 6-6" fill="none" stroke="#fff" stroke-width="2.5"/></svg></div>
    <h3>SERVICES TWO</h3>
    <p>Lorem Ipsum is simply text of dummy text of the printing and type setting..</p>
    <svg class="more" width="18" height="18" viewBox="0 0 18 18"><path d="M3 3l6 5 6-5M3 10l6 5 6-5" fill="none" stroke="#333" stroke-width="2"/></svg>
  </div>

  <div class="service active" style="left:494px">
    <div class="icon"><svg width="62" height="62" viewBox="0 0 62 62"><ellipse cx="26" cy="12" rx="20" ry="7" fill="#fff"/><path d="M6 18c0 4 9 7 20 7s20-3 20-7v8c0 4-9 7-20 7S6 30 6 26zM6 32c0 4 9 7 20 7v8C15 47 6 44 6 40z" fill="#fff"/><circle cx="42" cy="40" r="10" fill="none" stroke="#fff" stroke-width="4"/><path d="M49 47l9 9" stroke="#fff" stroke-width="5"/></svg></div>
    <h3>SERVICES THREE</h3>
    <p>Lorem Ipsum is simply text of dummy text of the printing and type setting..</p>
    <svg class="more" width="18" height="18" viewBox="0 0 18 18"><path d="M3 3l6 5 6-5M3 10l6 5 6-5" fill="none" stroke="#e4353b" stroke-width="2"/></svg>
  </div>

  <div class="service" style="left:706px">
    <div class="icon"><svg width="60" height="62" viewBox="0 0 60 62"><path d="M30 14a14 14 0 0 0-8 25v7h16v-7a14 14 0 0 0-8-25z" fill="none" stroke="#333" stroke-width="3"/><path d="M24 51h12M26 56h8" stroke="#333" stroke-width="3"/><path d="M30 2v6M10 10l4 4M50 10l-4 4M4 28h6M50 28h6" stroke="#333" stroke-width="3"/></svg></div>
    <h3>SERVICES FOUR</h3>
    <p>Lorem Ipsum is simply text of dummy text of the printing and type setting..</p>
    <svg class="more" width="18" height="18" viewBox="0 0 18 18"><path d="M3 3l6 5 6-5M3 10l6 5 6-5" fill="none" stroke="#333" stroke-width="2"/></svg>
  </div>

  <div class="service" style="left:921px">
    <div class="icon"><svg width="64" height="56" viewBox="0 0 64 56"><rect x="3" y="3" width="52" height="36" rx="2" fill="none" stroke="#333" stroke-width="3.5"/><path d="M22 39v8M36 39v8M16 49h26" stroke="#333" stroke-width="3.5"/><path d="M12 30V22M18 30V14M24 30V18M30 30V12" stroke="#333" stroke-width="3.5"/><circle cx="46" cy="36" r="8" fill="#fff" stroke="#333" stroke-width="3.5"/><path d="M52 42l8 8" stroke="#333" stroke-width="4"/></svg></div>
    <h3>SERVICES FIVE</h3>
    <p>Lorem Ipsum is simply text of dummy text of the printing and type setting..</p>
    <svg class="more" width="18" height="18" viewBox="0 0 18 18"><path d="M3 3l6 5 6-5M3 10l6 5 6-5" fill="none" stroke="#333" stroke-width="2"/></svg>
  </div>
</section>

<section class="introducers">
  <h2 class="section-title" style="top:52px">Our <span>Introducers</span></h2>
  <div class="intro-divider" style="left:412px"></div>
  <div class="intro-divider" style="left:768px"></div>

  <div class="intro-col" style="left:78px">
    <h4><b>?</b>Why become an introducer ?</h4>
    <p>Lorem Ipsum is simply dummy text of the printing and typesetting industry. Lorem Ipsum has been the industry's standard dummy text ever since the when an unknown printer took a galley of type and scrambled it to make a specimen book.</p>
    <div class="pill ghost">Contact us</div>
  </div>
  <div class="intro-col" style="left:435px">
    <h4><b>?</b>Who we help ?</h4>
    <p>Lorem Ipsum is simply dummy text of the printing and typesetting industry. Lorem Ipsum has been the industry's standard dummy text ever since the when an unknown printer took a galley of type and scrambled it to make a specimen book.</p>
    <div class="pill ghost">Contact us</div>
  </div>
  <div class="intro-col" style="left:791px">
    <h4><b>?</b>Why we are different ?</h4>
    <p>Lorem Ipsum is simply dummy text of the printing and typesetting industry. Lorem Ipsum has been the industry's standard dummy text ever since the when an unknown printer took a galley of type and scrambled it to make a specimen book.</p>
    <div class="pill ghost">Contact us</div>
  </div>
</section>

<h2 class="section-title" style="top:1993px">Contact <span>Us</span></h2>
<p class="lede" style="top:2050px">Lorem Ipsum is simply dummy text of the printing and typesetting industry. Lorem Ipsum has been the industry's standard dummy text ever since the 1500s, when an unknown printer took.</p>
<div class="field focus" style="left:153px;top:2118px;width:293px;height:51px">Name*</div>
<div class="field" style="left:455px;top:2118px;width:290px;height:51px">Email*</div>
<div class="field" style="left:756px;top:2118px;width:290px;height:51px">Phone*</div>
<div class="field" style="left:153px;top:2178px;width:893px;height:104px">Message*</div>
<div class="pill solid" style="left:517px;top:2295px;width:166px;height:57px;font-size:20px;font-weight:500">Submit</div>

<footer class="footer">
  <h5 style="left:78px">Usefull links</h5>
  <ul class="links">
    <li>Home</li><li>About Us</li><li>Services</li><li>Introducer</li><li>Contact Us</li>
  </ul>

  <h5 style="left:343px">Get in touch</h5>
  <div class="touch">
    <div class="row">
      <svg width="18" height="22" viewBox="0 0 18 22"><path d="M9 1a7 7 0 0 0-7 7c0 5 7 13 7 13s7-8 7-13a7 7 0 0 0-7-7z" fill="none" stroke="#e4353b" stroke-width="2"/><circle cx="9" cy="8" r="2.5" fill="#e4353b"/></svg>
      <div><b style="font-weight:400">HERON</b><br>Lorem ipsum dolor amet simple. Dummy text of printting &amp; type setting industry.</div>
    </div>
    <div class="row">
      <svg width="18" height="18" viewBox="0 0 18 18"><path d="M4 1l3 4-2 2a10 10 0 0 0 6 6l2-2 4 3-2 3C8 17 1 10 1 3z" fill="none" stroke="#e4353b" stroke-width="1.8"/></svg>
      <div>123 456 789</div>
    </div>
    <div class="row">
      <svg width="18" height="16" viewBox="0 0 18 16"><rect x="1" y="2" width="16" height="12" rx="1" fill="none" stroke="#e4353b" stroke-width="1.8"/><path d="M1 3l8 6 8-6" fill="none" stroke="#e4353b" stroke-width="1.8"/></svg>
      <div>info@herontrade.example</div>
    </div>
  </div>

  <h5 style="left:608px">Newsletter</h5>
  <div class="map" role="img" aria-label="Street map showing the office location with a red pin"></div>

  <h5 style="left:873px">Newsletter</h5>
  <p class="newsletter-text">Would you like to receive exclusive access to articles, white papers and our regular monthly newsletter?</p>
  <div class="email-input">Email Id</div>
  <div class="pill solid" style="left:873px;top:190px;width:166px;height:46px;font-size:18px">Subscribe</div>
</footer>

<div class="copyright">&copy;<b>HERON</b> - 2016 All rights reserved.</div>

</body>
</html>
```